Global social media analytics company needs business card design

We need an updated business card design to align with our new website - brightquillo.net -

I would also like a favicon designed as well.

Target Market(s)

CEOs, CMOs go big companies

Industry/Entity Type

Business

Contact Information for Business Card

Room for the following:
Address
Main telephone
Direct telephone or cell phone
twitter handle

Colors
aaaaaa

Requirements
Must have
• Attention to detail; style.
• Use the logo color from our website - which is gray

```html
<!DOCTYPE html>
<html lang="en">
<head>
<meta charset="utf-8">
<title>Brightquillo Stationery</title>
<link href="https://fonts.googleapis.com/css2?family=Open+Sans:wght@400;600&display=swap" rel="stylesheet">
<style>
  :root {
    --backdrop: #e8e8e8;
    --paper: #ffffff;
    --brand-gray: #8f8f8f;
    --band-text: #ffffff;
    --ink: #555555;
    --ink-soft: #7a7a7a;
    --rule: #bdbdbd;
  }
  * { box-sizing: border-box; margin: 0; padding: 0; }
  html, body { width: 1200px; height: 706px; overflow: hidden; }
  body {
    background: var(--backdrop);
    font-family: "Open Sans", Arial, sans-serif;
    color: var(--ink);
    position: relative;
  }
  .brand { display: flex; align-items: center; gap: 7px; font-weight: 600; letter-spacing: -0.2px; white-space: nowrap; }
  .brand-dot { border-radius: 50%; flex: none; }

  /* Business cards */
  .card {
    position: absolute;
    width: 290px; height: 166px;
    background: var(--paper);
    box-shadow: 0 2px 6px rgba(0,0,0,0.12);
    overflow: hidden;
  }
  .card-front { left: 150px; top: 150px; }
  .card-front .brand { position: absolute; left: 30px; top: 58px; font-size: 26px; color: var(--brand-gray); }
  .card-front .brand-dot { width: 34px; height: 34px; background: var(--brand-gray); }
  .card-front .web { position: absolute; right: 30px; bottom: 30px; font-size: 8px; color: var(--ink-soft); border-top: 1px solid var(--rule); padding-top: 3px; width: 140px; text-align: right; }

  .card-back { left: 150px; top: 370px; }
  .card-back .top-band { height: 44px; background: var(--brand-gray); padding: 10px 18px; }
  .card-back .brand { font-size: 18px; color: var(--band-text); }
  .card-back .brand-dot { width: 22px; height: 22px; background: var(--band-text); }
  .card-back .person { padding: 10px 18px 0; }
  .card-back .name { font-size: 12px; font-weight: 600; letter-spacing: 1.5px; color: var(--ink); }
  .card-back .role { font-size: 7px; color: var(--ink-soft); border-bottom: 1px solid var(--rule); padding-bottom: 4px; }
  .card-back .address { font-size: 6.5px; line-height: 1.4; color: var(--ink-soft); margin-top: 4px; }
  .card-back .contacts { position: absolute; right: 18px; top: 100px; font-size: 6.5px; line-height: 1.4; text-align: right; color: var(--ink-soft); }
  .card-back .bottom-band { position: absolute; left: 0; right: 0; bottom: 0; height: 16px; background: var(--brand-gray); color: var(--band-text); font-size: 6.5px; letter-spacing: 1px; padding: 3px 18px; white-space: nowrap; }

  /* Letterhead */
  .letterhead {
    position: absolute; left: 600px; top: 20px;
    width: 470px; height: 665px;
    background: var(--paper);
    box-shadow: 0 3px 10px rgba(0,0,0,0.14);
  }
  .letterhead .top-band {
    height: 72px; background: var(--brand-gray);
    display: flex; justify-content: space-between; align-items: center;
    padding: 0 28px;
  }
  .letterhead .brand { font-size: 22px; color: var(--band-text); }
  .letterhead .brand-dot { width: 30px; height: 30px; background: var(--band-text); }
  .letterhead .contact { display: flex; gap: 14px; font-size: 6.5px; line-height: 1.45; color: var(--band-text); white-space: nowrap; }
  .letterhead .letter { padding: 34px 44px 0 44px; font-size: 7.6px; line-height: 1.5; color: var(--ink); }
  .letterhead .sender { margin-bottom: 8px; }
  .letterhead .letter p { text-indent: 18px; margin-bottom: 12px; text-align: justify; }
  .letterhead .stamp { width: 110px; height: 46px; margin-top: 4px; }
  .letterhead .bottom-band {
    position: absolute; left: 0; right: 0; bottom: 0;
    height: 28px; background: var(--brand-gray); color: var(--band-text);
    font-size: 9px; letter-spacing: 2px; padding: 7px 28px; white-space: nowrap;
  }
</style>
</head>
<body>

  <div class="card card-front">
    <div class="brand"><span class="brand-dot"></span>brightquillo</div>
    <div class="web">www.brightquillo.net</div>
  </div>

  <div class="card card-back">
    <div class="top-band">
      <div class="brand"><span class="brand-dot"></span>brightquillo</div>
    </div>
    <div class="person">
      <div class="name">DANIEL HARPER</div>
      <div class="role">CEO</div>
      <div class="address">220 Linden Street, 3rd Fl<br>Oakford, MA 01999<br>USA</div>
    </div>
    <div class="contacts">
      +1 555 014 2290<br>+1 555 014 7731<br>@brightquillo<br>www.brightquillo.net
    </div>
    <div class="bottom-band">Clear Signals for Every Next Step</div>
  </div>

  <div class="letterhead">
    <div class="top-band">
      <div class="brand"><span class="brand-dot"></span>brightquillo</div>
      <div class="contact">
        <div>+1 555 014 2290<br>+1 555 014 7731<br>@brightquillo</div>
        <div>220 Linden Street, 3rd Fl<br>Oakford, MA 01999 USA<br>www.brightquillo.net</div>
      </div>
    </div>
    <div class="letter">
      <div class="sender">Brightquillo<br>December 22, 2011/Revised February 2, 2013</div>
      <p>Lorem ipsum dolor sit amet, consectetur adipiscing elit. Sed libero est, pellentesque facilisis tempor eu, pulvinar vitae justo. Praesent bibendum ultricies magna luctus luctus. Suspendisse potenti. Pellentesque habitant morbi tristique senectus et netus et malesuada fames ac turpis egestas. Nullam elit urna, porttitor quis luctus ac, gravida in ante.</p>
      <p>Donec consectetur tempor purus. Nullam turpis lacus, molestie bibendum auctor non, convallis quis mauris. Cum sociis natoque penatibus et magnis dis parturient montes, nascetur ridiculus mus. Aenean feugiat erat sit amet massa semper ullamcorper. Etiam varius, velit et pretium lobortis, massa interdum nunc, eget congue nisl mauris vitae sapien. Nam vitae dui tortor, quis scelerisque velit.</p>
      <p>Donec consectetur tempor purus. Nullam turpis lacus, molestie bibendum auctor non, convallis quis mauris. Cum sociis natoque penatibus et magnis dis parturient montes, nascetur ridiculus mus. Aenean feugiat erat sit amet massa semper ullamcorper. Etiam varius, velit et pretium lobortis, massa interdum nunc, eget congue nisl mauris vitae sapien. Nam vitae dui tortor, quis scelerisque velit.</p>
      <p>Donec consectetur tempor purus. Nullam turpis lacus, molestie bibendum auctor non, convallis quis mauris. Cum sociis natoque penatibus et magnis dis parturient montes, nascetur ridiculus mus. Aenean feugiat erat sit amet massa semper ullamcorper. Etiam varius, velit et pretium lobortis, massa interdum nunc, eget congue nisl mauris vitae sapien. Nam vitae dui tortor, quis scelerisque velit.</p>
      <svg class="stamp" role="img" aria-label="Approval stamp with handwritten signature" viewBox="0 0 110 46">
        <rect width="110" height="46" rx="6" fill="#ecebf2"/>
      </svg>
    </div>
    <div class="bottom-band">Clear Signals for Every Next Step</div>
  </div>

</body>
</html>
```